Business card and letterhead
Larkfield Harbor Consulting
I need double sided standard sized Business Card [3.5" x 2"]
Try the font from our new logo, but another font may look better - you decide
Professional
Marta J. Oakhurst, M.A., M.P.H.
President
3186 SE Quarry Lane #215
Seattle, WA 98107
marta@larkfieldharborconsulting.com
www.larkfieldharborconsulting.com
Please place the tagline on the backside below the website address.
We want this design to be used for all employee business cards.

```html
<!DOCTYPE html>
<html lang="en">
<head>
<meta charset="utf-8">
<title>Larkfield Harbor Consulting — Stationery</title>
<link rel="stylesheet" href="https://fonts.googleapis.com/css2?family=Cinzel:wght@600&family=Open+Sans:wght@400;600&display=swap">
<style>
  :root {
    --bg: #e9e6e1;
    --paper: #ffffff;
    --green: #2f6b3b;
    --green-dark: #24552e;
    --brown: #7b4b2b;
    --ink: #4a4a4a;
    --muted: #8a8a8a;
    --faint: #f1ede8;
    --brand-font: "Cinzel", Georgia, serif;
    --body-font: "Open Sans", Arial, sans-serif;
  }
  * { box-sizing: border-box; margin: 0; padding: 0; }
  html, body { width: 1200px; height: 437px; overflow: hidden; }
  body { background: var(--bg); position: relative; font-family: var(--body-font); color: var(--ink); }
  .piece { position: absolute; background: var(--paper); box-shadow: 0 2px 6px rgba(0,0,0,.18); overflow: hidden; }

  .brand { display: flex; flex-direction: column; align-items: center; gap: 3px; text-align: center; }
  .brand-dot { width: 12px; height: 12px; border-radius: 50%; background: var(--brown); }
  .brand-name { font-family: var(--brand-font); font-weight: 600; color: var(--green); line-height: 1.1; letter-spacing: .04em; }

  /* business cards */
  .card { left: 28px; width: 172px; height: 96px; }
  .card-label { position: absolute; left: 28px; width: 172px; text-align: center; font-size: 6px; color: var(--muted); }
  .card-front .brand { margin-top: 12px; }
  .card-front .brand-name { font-size: 10px; }
  .card-front .name-bar { position: absolute; left: 0; right: 0; bottom: 14px; height: 18px; background: var(--green); color: #fff; font-size: 6.5px; display: flex; flex-direction: column; justify-content: center; align-items: center; line-height: 1.2; }
  .card-back { padding: 12px 14px; font-size: 5.5px; line-height: 1.55; }
  .card-back .name { font-weight: 600; color: var(--green); font-size: 6.5px; }
  .card-back .tagline { margin-top: 6px; font-style: italic; color: var(--brown); }
  .card-green { background: var(--green); }
  .card-green .brand { margin-top: 18px; }
  .card-green .brand-dot { background: #fff; }
  .card-green .brand-name { color: #fff; font-size: 10px; }
  .card-green .web { position: absolute; bottom: 10px; width: 100%; text-align: center; font-size: 5.5px; color: #e6efe7; }

  /* letterheads */
  .letter { top: 29px; width: 272px; height: 352px; }
  .letter-one { left: 221px; }
  .letter-two { left: 509px; }
  .letter .brand { position: absolute; left: 18px; top: 18px; width: 84px; }
  .letter .brand-name { font-size: 8.5px; }
  .letter .address { position: absolute; left: 140px; top: 18px; font-size: 4.5px; line-height: 1.6; color: var(--muted); border-left: 1px solid var(--green); padding-left: 5px; }
  .letter .watermark { position: absolute; left: 86px; top: 125px; width: 100px; height: 100px; border-radius: 50%; background: var(--faint); }
  .letter .footer-band { position: absolute; left: 0; right: 0; bottom: 20px; height: 8px; background: var(--green); border-top: 2px solid var(--brown); }
  .letter .footer-text { position: absolute; bottom: 8px; width: 100%; text-align: center; font-size: 4.5px; color: var(--muted); }
  .letter-caption { position: absolute; top: 388px; font-size: 6px; color: var(--muted); width: 272px; text-align: center; }

  /* envelopes */
  .envelope { left: 822px; width: 354px; height: 100px; }
  .env-brown { top: 29px; }
  .env-green { top: 139px; }
  .env-white { top: 249px; height: 92px; }
  .env-back { top: 330px; left: 860px; width: 316px; height: 90px; }
  .envelope svg.flap { position: absolute; left: 0; top: 0; width: 100%; height: 48px; }
  .envelope .web { position: absolute; top: 68px; width: 100%; text-align: center; font-size: 5px; color: var(--muted); }
  .env-white .brand { position: absolute; left: 14px; top: 10px; width: 80px; }
  .env-white .brand-name { font-size: 7.5px; }
  .env-white .address { position: absolute; left: 14px; top: 52px; font-size: 4.5px; line-height: 1.6; color: var(--muted); }
  .env-white .rule { position: absolute; left: 0; right: 0; bottom: 0; height: 4px; background: var(--green); }
  .env-back .watermark { position: absolute; right: 60px; top: 20px; width: 56px; height: 56px; border-radius: 50%; background: var(--faint); }
</style>
</head>
<body>

  <!-- Business cards -->
  <section class="piece card card-front" style="top:30px">
    <div class="brand"><span class="brand-dot"></span><span class="brand-name">LARKFIELD HARBOR<br>CONSULTING</span></div>
    <div class="name-bar"><span>Marta J. Oakhurst, M.A., M.P.H.</span><span>President</span></div>
  </section>
  <p class="card-label" style="top:128px">Front side</p>

  <section class="piece card card-back" style="top:142px">
    <p class="name">Marta J. Oakhurst, M.A., M.P.H.</p>
    <p>President</p>
    <p>3186 SE Quarry Lane #215, Seattle, WA 98107</p>
    <p>206.555.0148</p>
    <p>marta@larkfieldharborconsulting.com</p>
    <p>www.larkfieldharborconsulting.com</p>
    <p class="tagline">Building healthier communities together</p>
  </section>
  <p class="card-label" style="top:240px">Back side</p>

  <section class="piece card card-green" style="top:254px">
    <div class="brand"><span class="brand-dot"></span><span class="brand-name">LARKFIELD HARBOR<br>CONSULTING</span></div>
    <p class="web">www.larkfieldharborconsulting.com</p>
  </section>
  <p class="card-label" style="top:352px">Alternate back side</p>

  <!-- Letterheads -->
  <section class="piece letter letter-one">
    <div class="brand"><span class="brand-dot"></span><span class="brand-name">LARKFIELD HARBOR<br>CONSULTING</span></div>
    <div class="address">
      <p>3186 SE Quarry Lane #215</p>
      <p>Seattle, WA 98107</p>
      <p>206.555.0148</p>
      <p>marta@larkfieldharborconsulting.com</p>
    </div>
    <div class="watermark" role="img" aria-label="Faint brand mark"></div>
    <div class="footer-band"></div>
    <p class="footer-text">www.larkfieldharborconsulting.com</p>
  </section>
  <p class="letter-caption" style="left:221px">Letterhead</p>

  <section class="piece letter letter-two">
    <div class="watermark" role="img" aria-label="Faint brand mark"></div>
    <div class="footer-band"></div>
    <p class="footer-text">www.larkfieldharborconsulting.com</p>
  </section>
  <p class="letter-caption" style="left:509px">Second page</p>

  <!-- Envelopes -->
  <section class="piece envelope env-brown">
    <svg class="flap" viewBox="0 0 354 48" preserveAspectRatio="none"><polygon points="0,0 354,0 354,10 177,48 0,10" fill="var(--brown)"/></svg>
    <p class="web">www.larkfieldharborconsulting.com</p>
  </section>

  <section class="piece envelope env-green">
    <svg class="flap" viewBox="0 0 354 48" preserveAspectRatio="none"><polygon points="0,0 354,0 354,10 177,48 0,10" fill="var(--green)"/></svg>
    <p class="web">www.larkfieldharborconsulting.com</p>
  </section>

  <section class="piece envelope env-white">
    <div class="brand"><span class="brand-dot"></span><span class="brand-name">LARKFIELD HARBOR<br>CONSULTING</span></div>
    <div class="address">
      <p>3186 SE Quarry Lane #215</p>
      <p>Seattle, WA 98107</p>
    </div>
    <div class="rule"></div>
  </section>

  <section class="piece envelope env-back">
    <svg class="flap" viewBox="0 0 316 48" preserveAspectRatio="none"><polyline points="0,0 158,44 316,0" fill="none" stroke="#dcdcdc" stroke-width="1"/></svg>
    <div class="watermark" role="img" aria-label="Faint brand mark"></div>
  </section>

</body>
</html>
```